Card for invoking rights with police

Our criminal defense law firm is seeking proposals for a design for our card intended for clients to carry with them in their car. Upon being pulled over, they would hand this card to the officer.
Text for the back of the card:
"For Law Enforcement:"
"I will comply with lawful orders but respectfully decline any test or other requests without my attorney. I wish to remain silent, do not consent to searches, and request to speak with my attorney now.
The back of the card should prominently feature the text and the firm logo should be secondary.
Front
Must prominently feature contact info: 503-555-0182. Do not include attorney name, email, phone from the example file. This is intended to be generic for the firm and not tied to an individual lawyer.
Included for design reference: current business card, firm logo.
We intend to use trenvo.com to produce the cards.
Updates
The back of the card should prominently display the text regarding invocation of rights. Please title it "For Law Enforcement".
Target Market(s)
People who have been stopped by police
Contact Information for Business Card
see project description
Look and feel

```html
<!DOCTYPE html>
<html lang="en">
<head>
<meta charset="utf-8">
<title>Harrow Law Firm – Rights Card</title>
<link href="https://fonts.googleapis.com/css2?family=Cinzel:wght@600&family=Lato:ital,wght@0,400;0,700;1,400&display=swap" rel="stylesheet">
<style>
  :root {
    --navy: #023050;
    --white: #ffffff;
    --backdrop: #8e8e8e;
  }
  * { box-sizing: border-box; margin: 0; padding: 0; }
  html, body {
    width: 1039px; height: 1200px; overflow: hidden;
    background: var(--backdrop);
  }
  .stage { position: relative; width: 1039px; height: 1200px; }
  .card {
    position: absolute; left: 124px; width: 783px; height: 446px; overflow: hidden;
  }
  .card--front { top: 93px; background: var(--navy); color: var(--white); }
  .card--back { top: 634px; background: var(--white); color: var(--navy); }

  .edge-notch { position: absolute; right: 0; top: 89px; }

  .identity { position: absolute; right: 69px; top: 84px; text-align: right; }
  .identity__name {
    font-family: "Cinzel", serif; font-weight: 600; font-size: 29px; letter-spacing: 0.5px; line-height: 1.1;
  }
  .identity__title {
    font-family: "Lato", sans-serif; font-style: italic; font-size: 20px; margin-top: 4px;
  }

  .contact { position: absolute; right: 69px; top: 194px; list-style: none;
    font-family: "Lato", sans-serif; font-size: 17px; letter-spacing: 0.2px; }
  .contact__item { display: flex; justify-content: flex-end; align-items: flex-start; line-height: 27px; }
  .contact__item--address { margin-bottom: 6px; }
  .contact__item--main { font-size: 22px; font-weight: 700; line-height: 32px; margin-bottom: 2px; }
  .contact__item--main .contact__icon { margin-top: 9px; }
  .contact__text { text-align: right; }
  .contact__icon { width: 14px; height: 14px; margin-left: 20px; margin-top: 6px; flex: none; }

  .brand {
    position: absolute; left: 0; right: 0; top: 48px;
    display: flex; justify-content: center; align-items: center; gap: 12px;
  }
  .brand__mark { width: 26px; height: 26px; background: var(--navy); }
  .brand__name {
    font-family: "Lato", sans-serif; font-weight: 400; font-size: 22px; letter-spacing: 3px; color: var(--navy);
  }
  .rights-title {
    position: absolute; left: 0; right: 0; top: 138px; text-align: center;
    font-family: "Lato", sans-serif; font-weight: 700; font-size: 34px; letter-spacing: 0.5px; color: var(--navy);
  }
  .rights {
    position: absolute; left: 40px; right: 40px; top: 212px; text-align: center;
    font-family: "Lato", sans-serif; font-size: 22px; line-height: 34px; color: var(--navy);
  }
</style>
</head>
<body>
<main class="stage">
  <section class="card card--front" aria-label="Card front">
    <svg class="edge-notch" width="24" height="54" viewBox="0 0 24 54" aria-hidden="true">
      <polygon points="24,0 24,54 0,27" fill="var(--white)"/>
    </svg>

    <div class="identity">
      <h1 class="identity__name">HARROW LAW FIRM</h1>
      <p class="identity__title">Criminal Defense</p>
    </div>

    <ul class="contact">
      <li class="contact__item contact__item--address">
        <span class="contact__text">2150 Cedar Point Ave<br>Suite 210, Larkview, WA 98400</span>
        <svg class="contact__icon" viewBox="0 0 14 14" aria-hidden="true"><path d="M7 0.5a4.6 4.6 0 0 0-4.6 4.6C2.4 8.5 7 13.5 7 13.5s4.6-5 4.6-8.4A4.6 4.6 0 0 0 7 0.5zm0 6.6a2 2 0 1 1 0-4 2 2 0 0 1 0 4z" fill="var(--white)"/></svg>
      </li>
      <li class="contact__item contact__item--main">
        <span class="contact__text">503-555-0182</span>
        <svg class="contact__icon" viewBox="0 0 14 14" aria-hidden="true"><path d="M3 1l2.2 2.6-1.2 1.6c.8 1.8 2.1 3.1 3.9 3.9l1.6-1.2L12 10l-1.4 2.5C6 12.3 1.7 8 1.4 3.4z" fill="var(--white)"/><path d="M8.5 1.5a4 4 0 0 1 4 4M8.3 3.5a2 2 0 0 1 2.2 2" stroke="var(--white)" stroke-width="1.1" fill="none"/></svg>
      </li>
      <li class="contact__item">
        <span class="contact__text">503-555-0147</span>
        <svg class="contact__icon" viewBox="0 0 14 14" aria-hidden="true"><rect x="3" y="0.5" width="8" height="13" rx="1.3" fill="var(--white)"/><rect x="4.3" y="2.2" width="5.4" height="8" fill="var(--navy)"/><circle cx="7" cy="11.8" r="0.7" fill="var(--navy)"/></svg>
      </li>
      <li class="contact__item">
        <span class="contact__text">503-555-0169</span>
        <svg class="contact__icon" viewBox="0 0 14 14" aria-hidden="true"><rect x="3.5" y="1" width="7" height="3.5" fill="var(--white)"/><rect x="1" y="5" width="12" height="5.5" rx="1" fill="var(--white)"/><rect x="3.5" y="8.5" width="7" height="4.5" fill="var(--white)" stroke="var(--navy)" stroke-width="0.8"/></svg>
      </li>
      <li class="contact__item">
        <span class="contact__text">harrowlawfirm.com</span>
        <svg class="contact__icon" viewBox="0 0 14 14" aria-hidden="true"><circle cx="7" cy="7" r="6.5" fill="var(--white)"/><path d="M3 4.5c1.5-.5 2 .8 3 1.5s-.5 2 .5 3-1 2.5-1.5 3M9 2.5c-.5 1 .5 1.5 1.5 2s1.5 2 .5 3" stroke="var(--navy)" stroke-width="1.1" fill="none"/></svg>
      </li>
    </ul>
  </section>

  <section class="card card--back" aria-label="Card back">
    <div class="brand">
      <span class="brand__mark" aria-hidden="true"></span>
      <span class="brand__name">Harrow Law Firm</span>
    </div>
    <h2 class="rights-title">For Law Enforcement:</h2>
    <p class="rights">I will comply with lawful orders but respectfully decline any test or other requests without my attorney. I wish to remain silent, do not consent to searches, and request to speak with my attorney now.</p>
  </section>
</main>
</body>
</html>
```